New Optometry Practice needs a Business Card

Need a business card for an Optometry practice called 'Marlow Vista Eyecare'. I would like to use designs that are friendly, fun and professional. Looking to incorporate glasses (see uploaded image). Not interested in design with an 'eye' in logo. Like green, blue, white as color choices..but open to your ideas. Back of card will be an appointment card as well as provide address, phone and email information.

Industry/Entity Type

Business

Contact Information for Business Card

Marlow Vista Eyecare
Dr. Petra Lindqvist, Optometrist (or O.D.)
4172 S Corbell Ave Wenatchee, WA 98736
PMarlowvistaeyecare.example

Colors
acd036
33b8a4
f68d4e
cfeae6
fee18a
cadf82

Requirements
Must have
• Appointment card on back with date/time of return for next exam

```html
<!DOCTYPE html>
<html lang="en">
<head>
<meta charset="utf-8">
<title>Marlow Vista Eyecare – Business Card</title>
<link rel="stylesheet" href="https://fonts.googleapis.com/css2?family=Open+Sans:wght@400;600&display=swap">
<style>
  :root {
    --stage: #1c1c1c;
    --card-front: #f3f3f3;
    --card-back-top: #fafafa;
    --card-white: #ffffff;
    --brand-blue: #3a9fd8;
    --ink: #111111;
  }
  * { box-sizing: border-box; margin: 0; padding: 0; }
  html, body { width: 1200px; height: 900px; overflow: hidden; }
  body {
    background: var(--stage);
    font-family: "Open Sans", Arial, sans-serif;
    color: var(--ink);
    position: relative;
  }
  .card {
    position: absolute;
    top: 184px;
    height: 490px;
    overflow: hidden;
  }
  .card--front {
    left: 299px; width: 301px;
    background: var(--card-front);
    border-radius: 12px;
  }
  .card--back {
    left: 645px; width: 305px;
    background: var(--card-white);
    border-radius: 12px 12px 0 0;
  }
  .brand-dot {
    position: absolute;
    left: 120px; top: 40px;
    width: 60px; height: 60px;
    border-radius: 50%;
    background: var(--brand-blue);
  }
  .wordmark {
    position: absolute;
    color: var(--brand-blue);
    font-weight: 400;
    text-align: right;
    line-height: 1;
  }
  .wordmark span { display: block; }
  .wordmark .line-main { letter-spacing: -0.5px; }
  .wordmark .line-sub { letter-spacing: 2px; margin-top: 6px; }
  .card--front .wordmark { left: 22px; top: 126px; width: 256px; }
  .card--front .line-main { font-size: 37px; }
  .card--front .line-sub { font-size: 25px; }
  .card--back .wordmark { left: 28px; top: 66px; width: 244px; }
  .card--back .line-main { font-size: 35px; }
  .card--back .line-sub { font-size: 23px; }

  .person { position: absolute; top: 250px; width: 100%; text-align: center; }
  .person-name { color: var(--brand-blue); font-weight: 600; font-size: 18px; letter-spacing: 0.3px; }
  .person-role { font-size: 13px; margin-top: 4px; }

  .address { position: absolute; top: 329px; width: 100%; text-align: center; font-size: 13px; line-height: 21px; }

  .contacts { position: absolute; top: 396px; width: 100%; text-align: center; font-size: 13px; line-height: 20.5px; list-style: none; }
  .contacts svg { width: 10px; height: 10px; vertical-align: -1px; margin-right: 3px; fill: var(--brand-blue); }

  .back-upper { position: absolute; left: 0; top: 0; width: 100%; height: 339px; background: var(--card-back-top); }
  .appointment { position: absolute; top: 346px; left: 0; width: 100%; }
  .appointment-title { text-align: center; color: var(--brand-blue); font-weight: 600; font-size: 16px; }
  .field-row { position: absolute; left: 18px; white-space: nowrap; font-size: 14px; }
  .field-row--name { top: 38px; }
  .field-row--when { top: 80px; }
  .field-label { color: var(--brand-blue); font-weight: 600; }
  .field-dots { color: var(--ink); font-weight: 600; letter-spacing: -0.6px; }
</style>
</head>
<body>
  <section class="card card--front" aria-label="Business card front">
    <div class="brand-dot"></div>
    <h1 class="wordmark"><span class="line-main">MARLOW VISTA</span><span class="line-sub">EYECARE</span></h1>
    <div class="person">
      <p class="person-name">DR. PETRA LINDQVIST</p>
      <p class="person-role">Optometrist</p>
    </div>
    <address class="address" style="font-style:normal">4172 S Corbell Ave<br>Wenatchee, WA 98736</address>
    <ul class="contacts">
      <li><svg viewBox="0 0 10 10"><path d="M2 0.5 L3.6 0.5 L4.2 2.8 L3 3.7 C3.6 5 4.9 6.4 6.3 7 L7.2 5.8 L9.5 6.4 L9.5 8 C9.5 9 8.8 9.5 8 9.5 C4 9.2 0.8 6 0.5 2 C0.5 1.2 1.1 0.5 2 0.5 Z"/></svg>(509) 555-0148</li>
      <li><svg viewBox="0 0 10 10"><path d="M0.5 2 H9.5 V8.5 H0.5 Z M1 2.4 L5 5.6 L9 2.4" stroke="#f3f3f3" stroke-width="0.8"/></svg>hello@marlowvista.example</li>
      <li><svg viewBox="0 0 10 10"><circle cx="5" cy="5" r="4.5"/><path d="M0.5 5 H9.5 M5 0.5 C3 3 3 7 5 9.5 M5 0.5 C7 3 7 7 5 9.5" stroke="#f3f3f3" stroke-width="0.7" fill="none"/></svg>www.PMarlowvistaeyecare.example</li>
    </ul>
  </section>

  <section class="card card--back" aria-label="Appointment card back">
    <div class="back-upper"></div>
    <h2 class="wordmark"><span class="line-main">MARLOW VISTA</span><span class="line-sub">EYECARE</span></h2>
    <div class="appointment">
      <p class="appointment-title">Appointment</p>
      <p class="field-row field-row--name"><span class="field-label">Name : </span><span class="field-dots">........................................................</span></p>
      <p class="field-row field-row--when"><span class="field-label">Date : </span><span class="field-dots">......................</span> <span class="field-label">Time : </span><span class="field-dots">.........................</span></p>
    </div>
  </section>
</body>
</html>
```